Stationary for a Consulting Firm
The Summit Compass Incorporated
Project: Stationary for a Consulting Firm
Stationary for a Consulting Firm - Consulting
Creative Brief
Professional
Dr. Gordon T. Feld
President
47 Maple Crest Okotoks, AB T2Q 4M9
gfeld@summitcompass.ca
www.summitcompass.ca
Business Cards, Stationary, Fax Cover Sheet, and Envelopes are required
Canada's Summit Compass

```html
<!DOCTYPE html>
<html lang="en">
<head>
<meta charset="utf-8">
<title>The Summit Compass Incorporated – Business Cards</title>
<link href="https://fonts.googleapis.com/css2?family=Montserrat:wght@800&family=Open+Sans:wght@400;600;700&display=swap" rel="stylesheet">
<style>
  :root {
    --bg: #e9ecef;
    --card-white: #ffffff;
    --blue: #1f93cf;
    --blue-light: #4cb8e6;
    --blue-deep: #157fba;
    --blue-pale: #bfe3f4;
    --ink: #4a4f55;
    --navy: #1b5f8f;
    --shadow: rgba(20, 40, 60, 0.18);
  }
  * { margin: 0; padding: 0; box-sizing: border-box; }
  html, body {
    width: 1200px; height: 1006px; overflow: hidden;
    background: var(--bg);
    font-family: "Open Sans", Arial, sans-serif;
  }
  .sheet {
    position: relative; width: 1200px; height: 1006px;
    display: flex; flex-direction: column; align-items: center;
    justify-content: center; gap: 52px;
  }
  .card {
    position: relative; width: 760px; height: 434px;
    border-radius: 22px; overflow: hidden;
    box-shadow: 0 10px 30px var(--shadow);
  }
  /* Front */
  .card-front { background: var(--card-white); }
  .front-band { position: absolute; inset: 0; width: 100%; height: 100%; }
  .brand {
    position: absolute; left: 58px; top: 52px;
    display: flex; align-items: center; gap: 16px;
  }
  .brand-dot {
    width: 58px; height: 58px; border-radius: 50%;
    background: var(--blue);
  }
  .brand-name {
    font-family: "Montserrat", Arial, sans-serif; font-weight: 800;
    font-size: 34px; line-height: 1.0; letter-spacing: 1px;
    color: var(--navy); text-transform: uppercase;
  }
  .contact-list {
    position: absolute; left: 60px; top: 150px;
    list-style: none;
  }
  .contact-item {
    display: flex; align-items: center; gap: 12px;
    font-size: 15px; color: var(--ink); height: 27px;
  }
  .contact-icon {
    width: 19px; height: 19px; border-radius: 50%;
    background: var(--blue); flex: none;
    display: flex; align-items: center; justify-content: center;
  }
  .contact-icon svg { width: 11px; height: 11px; fill: #fff; }
  .person {
    position: absolute; right: 44px; top: 290px; text-align: right;
  }
  .person-name { font-size: 17px; font-weight: 700; color: var(--navy); }
  .person-title { font-size: 13px; color: var(--ink); }
  .front-web {
    position: absolute; right: 44px; bottom: 26px;
    font-size: 15px; color: #fff; letter-spacing: 0.5px;
  }
  /* Back */
  .card-back {
    background: radial-gradient(ellipse at 30% 40%, var(--blue-light) 0%, var(--blue) 60%, var(--blue-deep) 100%);
  }
  .back-web {
    position: absolute; left: 250px; top: 52px;
    font-size: 15px; color: rgba(255,255,255,0.85); letter-spacing: 2px;
  }
  .back-mark {
    position: absolute; right: 70px; bottom: 50px;
    width: 150px; height: 150px; border-radius: 50%;
    background: rgba(255,255,255,0.14);
    border: 1px solid rgba(255,255,255,0.25);
  }
</style>
</head>
<body>
<main class="sheet">
  <section class="card card-front">
    <svg class="front-band" viewBox="0 0 760 434" preserveAspectRatio="none" aria-hidden="true">
      <path d="M0,380 L300,380 Q330,380 338,358 L350,340 Q358,326 385,326 L760,326 L760,434 L0,434 Z" fill="var(--blue-pale)"/>
      <path d="M0,392 L305,392 Q335,392 344,370 L352,354 Q360,340 388,340 L760,340 L760,434 L0,434 Z" fill="var(--blue)"/>
    </svg>
    <div class="brand">
      <div class="brand-dot"></div>
      <div class="brand-name">Summit<br>Compass</div>
    </div>
    <ul class="contact-list">
      <li class="contact-item"><span class="contact-icon"><svg viewBox="0 0 10 10"><path d="M5 0a3.5 3.5 0 0 0-3.5 3.5C1.5 6 5 10 5 10s3.5-4 3.5-6.5A3.5 3.5 0 0 0 5 0zm0 5a1.4 1.4 0 1 1 0-2.8A1.4 1.4 0 0 1 5 5z"/></svg></span>47 Maple Crest</li>
      <li class="contact-item"><span class="contact-icon" style="visibility:hidden"></span>Okotoks, AB T2Q 4M9</li>
      <li class="contact-item"><span class="contact-icon"><svg viewBox="0 0 10 10"><path d="M2 0.5l1.6 2-1 1.1a6 6 0 0 0 3.8 3.8l1.1-1 2 1.6-1 1.8C4.5 9.8 0.2 5.5 0.2 1.5z"/></svg></span>(587) 555-0134</li>
      <li class="contact-item"><span class="contact-icon"><svg viewBox="0 0 10 10"><path d="M2 0.5l1.6 2-1 1.1a6 6 0 0 0 3.8 3.8l1.1-1 2 1.6-1 1.8C4.5 9.8 0.2 5.5 0.2 1.5z"/></svg></span>(403) 555-0187</li>
      <li class="contact-item"><span class="contact-icon"><svg viewBox="0 0 10 10"><path d="M0.5 2h9v6h-9z M0.5 2l4.5 3.5L9.5 2" stroke="#1f93cf" stroke-width="0.8"/></svg></span>gfeld@summitcompass.ca</li>
      <li class="contact-item"><span class="contact-icon"><svg viewBox="0 0 10 10"><circle cx="5" cy="5" r="4.5"/><path d="M0.5 5h9M5 0.5v9" stroke="#1f93cf" stroke-width="0.8"/></svg></span>www.summitcompass.ca</li>
    </ul>
    <div class="person">
      <p class="person-name">Dr. Gordon T. Feld</p>
      <p class="person-title">President</p>
    </div>
    <p class="front-web">www.summitcompass.ca</p>
  </section>

  <section class="card card-back">
    <p class="back-web">www.summitcompass.ca</p>
    <div class="back-mark"></div>
  </section>
</main>
</body>
</html>
```